Market Intelligence Modules

Take the existing power point and add graphics to each slide and use photos and graphics to create a power point presentation that has the look and feel of a high tech company / research - with a theme of commercial real estate. To learn more about what the company does you can go to www.quarvelonix.com.

Target Market(s)

Target market are financial institutions and commercial real estate developers - going for high tech research look and feel and showing commercial real estate. ONLY commercial real estate.

Industry/Entity Type

Real Estate

Requirements
Must have
• Must have Quarvelonix logo and must communicate that Quarvelonix can process large amounts of data and analytics. Each slide should have some type of image that represents data or commercial real estate.
Should not have
• No blank white slides.

```html
<!DOCTYPE html>
<html lang="en">
<head>
<meta charset="utf-8">
<title>Quarvelonix – Market Intelligence Modules</title>
<link href="https://fonts.googleapis.com/css2?family=Open+Sans:wght@300;400;600;700&display=swap" rel="stylesheet">
<style>
:root{
  --sheet:#c9cbcd;
  --title-blue:#2a7fd0;
  --body:#4a4a4a;
  --green:#3ec43a;
  --dark:#3a3b3d;
  --royal:#2457e8;
  --deep-blue:#1a5fb0;
  --caption-blue:#4d93cf;
  --yellow:#f2ec1c;
  --orange:#ef7d2e;
}
*{margin:0;padding:0;box-sizing:border-box}
html,body{width:1200px;height:897px;overflow:hidden;background:var(--sheet);font-family:"Open Sans",Arial,sans-serif}
.deck{position:relative;width:1200px;height:897px}
.slide{position:absolute;width:357px;height:275px;overflow:hidden;
  background:linear-gradient(180deg,#ffffff 0%,#f3f4f5 55%,#e4e6e8 100%)}
.c1{left:50px}.c2{left:418px}.c3{left:787px}
.r1{top:24px}.r2{top:312px}.r3{top:606px}
.skyline{position:absolute;left:110px;right:0;bottom:4px;height:150px;
  background:linear-gradient(180deg,rgba(210,214,218,0) 0%,rgba(200,204,208,.55) 100%)}
.slide-title{position:absolute;left:15px;top:12px;font-weight:300;font-size:14.5px;color:var(--title-blue);letter-spacing:-.2px}
.rule{position:absolute;left:15px;right:15px;top:30px;height:1px;background:#b9bcc0}
.footer-bar{position:absolute;left:0;right:0;bottom:0;height:3px;background:var(--dark)}
.footer-green{position:absolute;right:0;bottom:0;width:97px;height:5px;background:var(--green)}
.page-no{position:absolute;right:6px;bottom:6px;font-size:4px;color:#888}
.brand-small{position:absolute;left:8px;bottom:8px;font-size:7px;font-weight:600;color:var(--green);letter-spacing:-.2px}

/* cover */
.cover{background:linear-gradient(180deg,#2b2c2e 0%,#4a4b4e 50%,#5a5b5e 100%)}
.cover-band{position:absolute;left:0;top:68px;width:357px;height:124px;
  background:linear-gradient(100deg,#1d3fe0 0%,#3a6cf5 50%,#2149d8 100%);clip-path:polygon(0 0,100% 0,100% 44%,205px 100%,0 100%)}
.cover-stripe{position:absolute;right:0;top:58px;width:120px;height:9px;background:var(--green);clip-path:polygon(8px 0,100% 0,100% 100%,0 100%)}
.cover-stripe2{position:absolute;left:190px;top:168px;width:30px;height:24px;background:var(--green);clip-path:polygon(22px 0,100% 0,8px 100%,0 100%)}
.cover-title{position:absolute;left:25px;top:121px;font-weight:300;font-size:14px;color:#e9eefc}
.cover-sub{position:absolute;left:28px;top:146px;font-size:6.5px;color:#b8c6f5;font-weight:300}
.cover-brand{position:absolute;right:20px;bottom:22px;font-size:21px;font-weight:400;color:var(--green);letter-spacing:-.6px}

/* zettabyte */
.map-photo{position:absolute;left:16px;top:48px;width:122px;height:90px;background:radial-gradient(ellipse at 50% 50%,#0f5fb8 0%,#08254a 55%,#020812 100%)}
.question-band{position:absolute;left:138px;top:54px;right:0;height:77px;background:#333436}
.question{position:absolute;left:161px;top:84px;font-size:12.5px;color:#fff;font-weight:400}
.facts{position:absolute;left:160px;top:149px;width:190px;list-style:none}
.facts li{font-size:6.6px;line-height:8.4px;color:var(--body);margin-bottom:9.5px;padding-left:5px;position:relative}
.facts li::before{content:"•";position:absolute;left:0;color:var(--title-blue)}

/* data environment */
.network-photo{position:absolute;left:16px;top:45px;width:326px;height:84px;
  background:linear-gradient(100deg,#7b2fc9 0%,#2f6fe0 35%,#3fb0e8 65%,#6fd6f2 100%)}
.terms{position:absolute;top:165px;list-style:none}
.terms li{font-size:8.5px;color:var(--body);height:18.4px;padding-left:10px;position:relative}
.terms li::before{content:"";position:absolute;left:0;top:4px;width:2.5px;height:2.5px;background:var(--title-blue)}
.terms.left{left:78px}.terms.right{left:194px}

/* objectives */
.marbles-photo{position:absolute;left:21px;top:94px;width:128px;height:72px;
  background:radial-gradient(ellipse at 45% 45%,#2d6fe0 0%,#9fc0ef 60%,#f4f6f8 100%)}
.objective-caption{position:absolute;left:18px;top:174px;width:134px;text-align:center;font-size:9.5px;line-height:12.4px;color:var(--caption-blue);font-weight:400}
.orb-label{font-family:"Open Sans",Arial,sans-serif;font-size:6px;fill:#fff;text-anchor:middle}

/* contact */
.contact-top{position:absolute;left:0;top:0;right:0;height:100px;background:#fff}
.contact-brand{position:absolute;left:23px;top:46px;font-size:21px;color:var(--green);letter-spacing:-.6px}
.contact-panel{position:absolute;left:0;top:106px;right:0;bottom:0;background:linear-gradient(90deg,#1f64b8 0%,#2b78c8 60%,#3d8fd6 100%)}
.contact-photo{position:absolute;right:0;top:106px;width:185px;bottom:0;background:linear-gradient(180deg,rgba(120,180,235,.0) 0%,rgba(90,160,225,.5) 100%)}
.contact-text{position:absolute;left:24px;top:138px;font-size:5.6px;line-height:7.4px;color:#cfe0f5;font-weight:300}
.contact-text p{margin-bottom:9px}
.social{display:flex;gap:3px;margin-top:3px}
.social span{width:8px;height:8px;background:#fff;display:block}
</style>
</head>
<body>
<main class="deck">

  <section class="slide cover c1 r1">
    <div class="cover-band" role="img" aria-label="Blue-tinted photo of a glass office tower"></div>
    <div class="cover-stripe"></div>
    <div class="cover-stripe2"></div>
    <h1 class="cover-title">Lorem ipsum dolor sit amet</h1>
    <p class="cover-sub">Birmingham, March 25, 2013</p>
    <div class="cover-brand">Quarvelonix</div>
  </section>

  <section class="slide c2 r1">
    <div class="skyline" role="img" aria-label="Faded photo of commercial towers"></div>
    <h2 class="slide-title">THE ZETTABYTE ERA</h2><div class="rule"></div>
    <div class="question-band"></div>
    <div class="map-photo" role="img" aria-label="Digital world map on a field of binary data"></div>
    <p class="question">What is a zettabyte?</p>
    <ul class="facts">
      <li>One zettabyte of data allows you to stack books from Earth to Pluto 20 times (72 billion miles)</li>
      <li>If one gigabyte of data were a cup of coffee a zettabyte would equal the Great Wall of China</li>
      <li>In 2015 all internet traffic will exceed one zettabyte of data - 540,000 time increase from 2003</li>
    </ul>
    <div class="brand-small">Quarvelonix</div>
    <div class="footer-bar"></div><div class="footer-green"></div>
  </section>

  <section class="slide c3 r1">
    <div class="skyline" role="img" aria-label="Faded photo of commercial towers"></div>
    <h2 class="slide-title">REAL WORLD DATA ENVIRONMENT</h2><div class="rule"></div>
    <div class="network-photo" role="img" aria-label="Glowing network of connected data nodes"></div>
    <ul class="terms left"><li>Overload</li><li>Unorganized</li><li>Disperse</li><li>Quantitative</li></ul>
    <ul class="terms right"><li>Qualitative</li><li>Relevance</li><li>Trends</li><li>Timeliness</li></ul>
    <div class="brand-small">Quarvelonix</div>
    <div class="footer-bar"></div><div class="footer-green"></div><span class="page-no">2</span>
  </section>

  <section class="slide c1 r2">
    <div class="skyline" role="img" aria-label="Faded photo of commercial towers"></div>
    <h2 class="slide-title">THE INTERPRETATION PROCESS</h2><div class="rule"></div>
    <svg width="357" height="275" style="position:absolute;left:0;top:0" aria-label="Five-step process">
      <defs>
        <linearGradient id="blueStep" x1="0" y1="0" x2="0" y2="1"><stop offset="0" stop-color="#2a86d8"/><stop offset="1" stop-color="#1559a8"/></linearGradient>
        <linearGradient id="darkStep" x1="0" y1="0" x2="0" y2="1"><stop offset="0" stop-color="#3d3e40"/><stop offset="1" stop-color="#232425"/></linearGradient>
      </defs>
      <g font-family="Open Sans, Arial, sans-serif" font-size="6" fill="#fff" text-anchor="middle">
        <polygon points="36,86 100,86 114,114 100,142 36,142 36,142" fill="url(#blueStep)"/>
        <polygon points="100,86 157,86 171,114 157,142 100,142 114,114" fill="url(#darkStep)"/>
        <polygon points="157,86 214,86 228,114 214,142 157,142 171,114" fill="url(#blueStep)"/>
        <polygon points="214,86 271,86 285,114 271,142 214,142 228,114" fill="url(#darkStep)"/>
        <polygon points="271,86 326,86 340,114 326,142 271,142 285,114" fill="url(#blueStep)"/>
        <text x="65" y="112">Database</text><text x="65" y="119">Integration</text>
        <text x="137" y="112">Quantitatve</text><text x="137" y="119">Research</text>
        <text x="192" y="112">Qualitative</text><text x="192" y="119">Research</text>
        <text x="249" y="112">Indexes</text><text x="249" y="119">Reports</text>
        <text x="305" y="106">Times</text><text x="305" y="113">Staped</text><text x="305" y="120">Market</text><text x="305" y="127">Updates</text>
      </g>
    </svg>
    <div class="brand-small">Quarvelonix</div>
    <div class="footer-bar"></div><div class="footer-green"></div>
  </section>

  <section class="slide c2 r2">
    <div class="skyline" role="img" aria-label="Faded photo of commercial towers"></div>
    <h2 class="slide-title">REPORT OBJECTIVES</h2><div class="rule"></div>
    <div class="marbles-photo" role="img" aria-label="Cluster of blue glass marbles with one red marble"></div>
    <p class="objective-caption">Consolidating information in formats that are under-standable, meaningful and actionable</p>
    <svg width="357" height="275" style="position:absolute;left:0;top:0" aria-label="Report objectives diagram">
      <g stroke="#9a9c9f" stroke-width="2.5">
        <circle cx="255" cy="82" r="23" fill="#8c6a77"/>
        <circle cx="196" cy="143" r="23" fill="#9c7a66"/>
        <circle cx="254" cy="143" r="19" fill="#c7a891"/>
        <circle cx="315" cy="143" r="23" fill="#7a889a"/>
        <circle cx="256" cy="202" r="23" fill="#76a46c"/>
      </g>
      <text class="orb-label" x="255" y="84">Trending</text>
      <text class="orb-label" x="196" y="145">Relevance</text>
      <text class="orb-label" x="254" y="141">Indexes</text><text class="orb-label" x="254" y="148">Report</text>
      <text class="orb-label" x="315" y="145">Consilidated</text>
      <text class="orb-label" x="256" y="204">Timeliness</text>
    </svg>
    <div class="brand-small">Quarvelonix</div>
    <div class="footer-bar"></div><div class="footer-green"></div><span class="page-no">2</span>
  </section>

  <section class="slide c3 r2">
    <div class="skyline" role="img" aria-label="Faded photo of commercial towers"></div>
    <h2 class="slide-title">DATA REPORTING RESOURCES</h2><div class="rule"></div>
    <svg width="357" height="275" style="position:absolute;left:0;top:0" aria-label="Resource matrix table">
      <rect x="71" y="64" width="210" height="162" fill="#fff" stroke="#444" stroke-width=".6"/>
      <rect x="71" y="64" width="210" height="5" fill="#bdbdbd"/>
      <rect x="71" y="78" width="210" height="5" fill="var(--yellow)"/>
      <rect x="71" y="116" width="210" height="6" fill="var(--yellow)"/>
      <rect x="71" y="155" width="210" height="8" fill="var(--yellow)"/>
      <rect x="71" y="174" width="210" height="5" fill="var(--yellow)"/>
      <g stroke="#555" stroke-width=".35">
        <line x1="71" y1="78" x2="281" y2="78"/>
        <line x1="87" y1="64" x2="87" y2="226"/>
        <line x1="103" y1="69" x2="103" y2="226"/><line x1="119" y1="69" x2="119" y2="226"/>
        <line x1="135" y1="69" x2="135" y2="226"/><line x1="151" y1="69" x2="151" y2="226"/>
        <line x1="167" y1="69" x2="167" y2="226"/><line x1="183" y1="69" x2="183" y2="226"/>
        <line x1="199" y1="69" x2="199" y2="226"/><line x1="215" y1="69" x2="215" y2="226"/>
        <line x1="231" y1="69" x2="231" y2="226"/><line x1="247" y1="69" x2="247" y2="226"/>
        <line x1="263" y1="69" x2="263" y2="226"/>
        <line x1="71" y1="90" x2="281" y2="90"/><line x1="71" y1="97" x2="281" y2="97"/>
        <line x1="71" y1="104" x2="281" y2="104"/><line x1="71" y1="110" x2="281" y2="110"/>
        <line x1="71" y1="128" x2="281" y2="128"/><line x1="71" y1="135" x2="281" y2="135"/>
        <line x1="71" y1="142" x2="281" y2="142"/><line x1="71" y1="148" x2="281" y2="148"/>
        <line x1="71" y1="168" x2="281" y2="168"/><line x1="71" y1="186" x2="281" y2="186"/>
        <line x1="71" y1="193" x2="281" y2="193"/><line x1="71" y1="200" x2="281" y2="200"/>
        <line x1="71" y1="207" x2="281" y2="207"/><line x1="71" y1="214" x2="281" y2="214"/>
        <line x1="71" y1="220" x2="281" y2="220"/>
      </g>
      <g font-family="Open Sans, Arial, sans-serif" font-size="2.4" fill="#222">
        <text x="72" y="74">Sector</text><text x="89" y="74">Region</text><text x="105" y="74">Office</text>
        <text x="121" y="74">Retail</text><text x="137" y="74">Industrial</text><text x="153" y="74">Apartment</text>
        <text x="169" y="74">Hotel</text><text x="185" y="74">Land</text>
        <text x="72" y="82">Market Studies</text><text x="72" y="121">Demographics</text>
        <text x="72" y="160">Property Indexes</text><text x="72" y="178">REIT Data</text>
      </g>
    </svg>
    <div class="brand-small">Quarvelonix</div>
    <div class="footer-bar"></div><div class="footer-green"></div><span class="page-no">2</span>
  </section>

  <section class="slide c1 r3">
    <div class="skyline" role="img" aria-label="Faded photo of commercial towers"></div>
    <h2 class="slide-title">REIT REPORT</h2><div class="rule"></div>
    <svg width="357" height="275" style="position:absolute;left:0;top:0" aria-label="REIT sales summary table and bar charts">
      <rect x="21" y="59" width="276" height="95" fill="#fff"/>
      <rect x="21" y="59" width="276" height="5" fill="var(--orange)"/>
      <rect x="21" y="64" width="276" height="4" fill="#d9d9d9"/>
      <g font-family="Open Sans, Arial, sans-serif" font-size="2.6" fill="#222">
        <text x="140" y="62.6" fill="#fff">Quarvelonix REIT Sales Summary</text>
        <text x="23" y="67">Sector</text><text x="112" y="67">Month</text><text x="140" y="67">Quarter</text>
        <text x="168" y="67">Year</text><text x="208" y="67">Prior</text><text x="250" y="67">Change</text>
        <text x="23" y="73">Office</text><text x="23" y="83">Retail</text><text x="23" y="93">Industrial</text>
        <text x="23" y="103">Apartment</text><text x="23" y="113">Hotel</text><text x="23" y="123">Healthcare</text>
        <text x="23" y="133">Storage</text><text x="23" y="143">Total</text>
      </g>
      <g fill="#fbd3b6">
        <rect x="21" y="75" width="90" height="3"/><rect x="21" y="95" width="90" height="3"/>
        <rect x="21" y="115" width="90" height="3"/><rect x="21" y="135" width="90" height="3"/>
      </g>
      <g stroke="#9a9a9a" stroke-width="1.2">
        <path d="M112 72h14M140 72h14M168 72h14M208 72h14M250 72h14M112 77h14M140 77h14M168 77h14M208 77h14M250 77h14M112 82h14M140 82h14M168 82h14M208 82h14M250 82h14M112 87h14M140 87h14M168 87h14M208 87h14M250 87h14M112 92h14M140 92h14M168 92h14M208 92h14M250 92h14M112 97h14M140 97h14M168 97h14M208 97h14M250 97h14M112 102h14M140 102h14M168 102h14M208 102h14M250 102h14M112 107h14M140 107h14M168 107h14M208 107h14M250 107h14M112 112h14M140 112h14M168 112h14M208 112h14M250 112h14M112 117h14M140 117h14M168 117h14M208 117h14M250 117h14M112 122h14M140 122h14M168 122h14M208 122h14M250 122h14M112 127h14M140 127h14M168 127h14M208 127h14M250 127h14M112 132h14M140 132h14M168 132h14M208 132h14M250 132h14M112 137h14M140 137h14M168 137h14M208 137h14M250 137h14M112 142h14M140 142h14M168 142h14M208 142h14M250 142h14M112 147h14M140 147h14M168 147h14M208 147h14M250 147h14"/>
      </g>
      <g stroke="#e33" stroke-width="1.2">
        <path d="M208 72h8M250 77h8M208 92h8M250 102h8M208 117h8M250 132h8M208 142h8"/>
      </g>
      <rect x="27" y="157" width="131" height="61" fill="#fff" opacity=".6"/>
      <rect x="160" y="157" width="135" height="61" fill="#fff" opacity=".6"/>
      <g fill="var(--orange)">
        <rect x="90" y="160" width="40" height="1.4"/><rect x="90" y="163" width="35" height="1.4"/>
        <rect x="90" y="166" width="32" height="1.4"/><rect x="90" y="169" width="28" height="1.4"/>
        <rect x="90" y="172" width="24" height="1.4"/><rect x="90" y="175" width="22" height="1.4"/>
        <rect x="90" y="178" width="20" height="1.4"/><rect x="90" y="181" width="18" height="1.4"/>
        <rect x="90" y="184" width="16" height="1.4"/><rect x="90" y="187" width="14" height="1.4"/>
        <rect x="90" y="190" width="12" height="1.4"/><rect x="90" y="193" width="10" height="1.4"/>
        <rect x="90" y="196" width="8" height="1.4"/><rect x="90" y="199" width="6" height="1.4"/>
        <rect x="85" y="202" width="5" height="1.4"/><rect x="78" y="205" width="12" height="1.4"/>
        <rect x="250" y="160" width="12" height="1.4"/><rect x="250" y="163" width="10" height="1.4"/>
        <rect x="250" y="166" width="8" height="1.4"/><rect x="246" y="169" width="4" height="1.4"/>
        <rect x="240" y="172" width="10" height="1.4"/><rect x="238" y="175" width="12" height="1.4"/>
        <rect x="236" y="178" width="14" height="1.4"/><rect x="234" y="181" width="16" height="1.4"/>
        <rect x="232" y="184" width="18" height="1.4"/><rect x="230" y="187" width="20" height="1.4"/>
        <rect x="228" y="190" width="22" height="1.4"/><rect x="226" y="193" width="24" height="1.4"/>
        <rect x="222" y="196" width="28" height="1.4"/><rect x="218" y="199" width="32" height="1.4"/>
        <rect x="214" y="202" width="36" height="1.4"/><rect x="208" y="205" width="42" height="1.4"/>
      </g>
    </svg>
    <div class="brand-small">Quarvelonix</div>
    <div class="footer-bar"></div><div class="footer-green"></div><span class="page-no">2</span>
  </section>

  <section class="slide c2 r3">
    <div class="skyline" role="img" aria-label="Faded photo of commercial towers"></div>
    <h2 class="slide-title">SOURCE SYNOPSIS</h2><div class="rule"></div>
    <svg width="357" height="275" style="position:absolute;left:0;top:0" aria-label="Grid of data source partner badges">
      <rect x="18" y="55" width="322" height="166" fill="#fff" stroke="#d6d8da" stroke-width=".6"/>
      <g fill="#c9ced6">
        <circle cx="49" cy="84" r="14"/><circle cx="98" cy="84" r="14"/><circle cx="155" cy="84" r="14"/>
        <circle cx="228" cy="84" r="14"/><circle cx="300" cy="84" r="14"/>
        <rect x="30" y="112" width="38" height="30" rx="2"/><rect x="82" y="120" width="46" height="12" rx="2"/>
        <rect x="140" y="114" width="42" height="22" rx="2"/><rect x="195" y="118" width="52" height="14" rx="2"/>
        <rect x="282" y="112" width="40" height="24" rx="2"/>
        <rect x="30" y="156" width="54" height="14" rx="2"/><rect x="98" y="156" width="70" height="10" rx="2"/>
        <rect x="178" y="150" width="30" height="22" rx="2"/><rect x="222" y="150" width="52" height="22" rx="2"/>
        <rect x="288" y="156" width="30" height="12" rx="2"/>
        <rect x="38" y="190" width="68" height="12" rx="2"/><rect x="118" y="186" width="52" height="18" rx="2"/>
        <rect x="184" y="188" width="74" height="14" rx="2"/><rect x="264" y="188" width="32" height="16" rx="2"/>
        <rect x="302" y="186" width="28" height="18" rx="2"/>
      </g>
    </svg>
    <div class="brand-small">Quarvelonix</div>
    <div class="footer-bar"></div><div class="footer-green"></div><span class="page-no">2</span>
  </section>

  <section class="slide c3 r3">
    <div class="contact-top"></div>
    <div class="contact-brand">Quarvelonix</div>
    <svg width="357" height="10" style="position:absolute;left:0;top:97px" aria-hidden="true">
      <polygon points="0,2 258,2 256,9 0,9" fill="var(--royal)"/>
      <polygon points="262,2 357,0 357,4 261,6" fill="var(--green)"/>
      <polygon points="260,6 357,4 357,9 258,9" fill="var(--royal)"/>
    </svg>
    <div class="contact-panel"></div>
    <div class="contact-photo" role="img" aria-label="Blue-toned photo of a curved glass office tower"></div>
    <div class="contact-text">
      <p>Quarvelonix – Downtown Marlowe<br>218 Lakeview Row<br>Suite 410<br>Marlowe, NV – 89917</p>
      <p>Quarvelonix – North / West Hills<br>1470 Orchard Park Drive<br>Suite 305<br>Brannock, NV – 89928</p>
      <div>● +1.415.555.0192<br>● info@quarvelonix.com<br>● www.quarvelonix.com</div>
      <div class="social"><span></span><span></span><span></span></div>
    </div>
  </section>

</main>
</body>
</html>
```